New Zealand Export company needs business cards

We need new business cards to match our new logo for a company based in New Zealand who deal specifically with the Pacific Islands. We source, consolidate and ship products out of New Zealand to the Pacific Islands. Will attach our old ones and also new logo.
Would like the Islands we deal with and the areas of work we have access to, to be included on the business cards.

Contact Information for Business Card

T +64 9 571 3048
F +64 9 571 6285
12-18 Kowhai Lane, Drury, 2113
PO Box 814, Drury, Auckland 2247, New Zealand
www.falconfreight.example.nz
E sales@falconfreight.example.nz

Font styles to use
Sans Serif

Colors
85abd2
33a6d7
ffffff

Requirements
Must have
• A company of PWM

```html
<!DOCTYPE html>
<html lang="en">
<head>
<meta charset="utf-8">
<title>Falcon Freight – Business Cards</title>
<link href="https://fonts.googleapis.com/css2?family=Roboto:wght@400;500;700&display=swap" rel="stylesheet">
<style>
  :root {
    --navy: #0d56a6;
    --sky: #33a6d7;
    --bright: #41bde9;
    --ink: #3a3a3a;
    --paper: #f6f6f6;
    --stage: #a9a9a9;
    --white: #ffffff;
  }
  * { margin: 0; padding: 0; box-sizing: border-box; }
  html, body { width: 1172px; height: 1200px; overflow: hidden; }
  body {
    background: var(--stage);
    font-family: "Roboto", Arial, sans-serif;
    position: relative;
  }
  .card {
    position: absolute;
    left: 214px;
    width: 744px;
    border-radius: 24px;
    overflow: hidden;
  }
  .card--front { top: 122px; height: 425px; }
  .card--back { top: 645px; height: 430px; background: var(--paper); }

  /* Front */
  .island-photo {
    position: absolute; inset: 0 0 49px 0;
    background: linear-gradient(180deg, #8fd6f3 0%, #c7ecf9 40%, #e6f6fc 60%, #9ed8dc 66%, #78c3c8 100%);
  }
  .brand-name {
    position: absolute; left: 0; right: 0;
    text-align: center;
    font-weight: 700; color: var(--navy);
    letter-spacing: 1px;
  }
  .card--front .brand-name { top: 54px; font-size: 46px; }
  .card--back .brand-name { top: 76px; font-size: 46px; }

  .list-heading {
    position: absolute; top: 162px;
    font-weight: 700; font-size: 20px; color: var(--navy);
  }
  .list-heading--islands { left: 27px; }
  .list-heading--industries { right: 26px; }

  .pick-list {
    position: absolute; top: 262px;
    list-style: none;
    font-size: 18px; line-height: 25px; color: #1d2a3a;
  }
  .pick-list--islands { left: 27px; }
  .pick-list--industries { right: 26px; text-align: right; }
  .dot { color: var(--navy); font-size: 14px; padding: 0 2px; }

  .tagline-band {
    position: absolute; left: 0; right: 0; bottom: 0; height: 49px;
    background: var(--navy);
    color: var(--white);
    font-weight: 700; font-size: 28px;
    display: flex; align-items: center; justify-content: center;
  }

  /* Back */
  .person-name {
    position: absolute; left: 0; right: 0; top: 197px;
    text-align: center; font-weight: 700; font-size: 28px; color: var(--navy);
  }
  .person-role {
    position: absolute; left: 0; right: 0; top: 232px;
    text-align: center; font-size: 19px; color: var(--ink);
  }
  .address {
    position: absolute; right: 399px; top: 287px;
    text-align: right; font-size: 18px; line-height: 24px; color: var(--ink);
    font-style: normal;
  }
  .contact-divider {
    position: absolute; left: 372px; top: 290px; width: 2px; height: 65px;
    background: var(--sky);
  }
  .contact-list {
    position: absolute; left: 398px; top: 287px;
    list-style: none; font-size: 18px; line-height: 24px; color: var(--ink);
  }
  .contact-list li { display: flex; align-items: center; gap: 9px; }
  .contact-list svg { width: 16px; height: 16px; flex: none; }

  .footer-band { position: absolute; left: 0; bottom: 0; width: 744px; height: 36px; }
  .web-address {
    position: absolute; left: 0; right: 0; bottom: 4px;
    text-align: center; font-size: 17px; color: var(--white);
  }
</style>
</head>
<body>

<section class="card card--front">
  <div class="island-photo" role="img" aria-label="Photo of a green tropical island in a turquoise sea under a bright sky"></div>
  <div class="brand-name">FALCON FREIGHT</div>

  <h2 class="list-heading list-heading--islands">ISLANDS</h2>
  <h2 class="list-heading list-heading--industries">INDUSTRIES</h2>

  <ul class="pick-list pick-list--islands">
    <li><span class="dot">●</span> Cook Islands <span class="dot">●</span>Papua New Guinea <span class="dot">●</span>Tahiti</li>
    <li><span class="dot">●</span> Tuvalu&nbsp; Tokelau <span class="dot">●</span>Fiji&nbsp;&nbsp; Kiribati <span class="dot">●</span>Samoa</li>
    <li><span class="dot">●</span> New Caledonia <span class="dot">●</span>Tonga <span class="dot">●</span>Norfolk Island</li>
    <li><span class="dot">●</span> Solomon Islands <span class="dot">●</span>Vanuatu</li>
  </ul>

  <ul class="pick-list pick-list--industries">
    <li>Hardware <span class="dot">●</span>Automotive <span class="dot">●</span></li>
    <li>Homewares <span class="dot">●</span>Aid Solutions <span class="dot">●</span></li>
    <li>Hospitality <span class="dot">●</span>Safety Equipment <span class="dot">●</span></li>
    <li>Environmental Resources <span class="dot">●</span></li>
  </ul>

  <div class="tagline-band">SUPPLYING THE PACIFIC FOR OVER 38 YEARS</div>
</section>

<section class="card card--back">
  <div class="brand-name">FALCON FREIGHT</div>

  <h1 class="person-name">TESSA LOWE</h1>
  <p class="person-role">Sales Manager</p>

  <address class="address">
    12-18 Kowhai Lane, Drury, 2113<br>
    PO Box 814, Drury, Auckland 2247<br>
    New Zealand
  </address>

  <div class="contact-divider"></div>

  <ul class="contact-list">
    <li>
      <svg viewBox="0 0 16 16" aria-hidden="true"><path d="M3 1.5l2.5 0 1 3.5-1.6 1.2a8 8 0 0 0 4.9 4.9l1.2-1.6 3.5 1v2.5c0 .8-.7 1.5-1.5 1.5A13 13 0 0 1 1.5 3c0-.8.7-1.5 1.5-1.5z" fill="none" stroke="#0d56a6" stroke-width="1.5" stroke-linejoin="round"/></svg>
      +64 9 571 3048
    </li>
    <li>
      <svg viewBox="0 0 16 16" aria-hidden="true"><rect x="4" y="1" width="8" height="14" rx="1.5" fill="none" stroke="#0d56a6" stroke-width="1.5"/><circle cx="8" cy="12.3" r="0.9" fill="#0d56a6"/></svg>
      +64 9 571 6285
    </li>
    <li>
      <svg viewBox="0 0 16 16" aria-hidden="true"><rect x="1" y="3" width="14" height="10" fill="#0d56a6"/><path d="M1 3l7 6 7-6M1 13l5-5M15 13l-5-5" fill="none" stroke="#f6f6f6" stroke-width="1"/></svg>
      sales@falconfreight.example.nz
    </li>
  </ul>

  <svg class="footer-band" viewBox="0 0 744 36" aria-hidden="true">
    <path d="M0 0H248L238 10H0Z" fill="#41bde9"/>
    <path d="M496 0H744V10H506Z" fill="#41bde9"/>
    <path d="M0 15H243L255 3H489L501 15H744V36H0Z" fill="#0d56a6"/>
  </svg>
  <div class="web-address">www.falconfreight.example.nz</div>
</section>

</body>
</html>
```